Your 'not so average' farmers. We are farmers and entrepreneurs trying to connect the great divide.

KTB (Brosmere Holdings Inc) is a family owned farm (in our 3rd generation). We grow vegetables (corn, soy, potatoes, snap beans) but we also invest in and grow businesses. These other businesses can be non-farming related businesses. We are family oriented, environmentally concise, and active in our small community. We need a business card to hand out to our fellow farmers, businesses we would like to partner with and invest in, and community members. So, we need a card with a natural, 'tenders of the land' feel for the farmers but no overly so that we seem centered on farming for the other businesses. We would like it to have our Company info (name, number, email, phone, fax) then Personal info for us five who run the joint (Name, phone, email). So we will order 100 cards for each 5 who work at KTB (500total) that is professional, not boring or hokey, but catching and unique.
Target Market(s)
Farmers, Business Owners, Investors, Community Members
Industry/Entity Type
Farming
Contact Information for Business Card
Office info on one side:
Brosmere Holdings Inc.
1187 Larkin Rd.
Pell Hollow, WI 54872
Office: (608) 555-0417
Fax: (608) 555-0283
brosmereoffice@quillpost.example
Personal Info for the 5 who run KTB. Everybody will have their own personal info on their cards(maybe on the other side):
Name
Mobile
Email
Look and feel

```html
<!DOCTYPE html>
<html lang="en">
<head>
<meta charset="utf-8">
<title>Brosmere Holdings Inc. — Business Card</title>
<link rel="stylesheet" href="https://fonts.googleapis.com/css2?family=Cinzel:wght@600&family=Crimson+Text:wght@400;600&family=Lato:wght@300&display=swap">
<style>
  :root {
    --stage: #2a2a2a;
    --gold: #f2b414;
    --gold-deep: #e9a40e;
    --gold-light: #f7c435;
    --cream: #ffe8b0;
    --brown: #5b1f0c;
    --red: #d52a18;
    --orange: #e0832a;
    --label-bg: #f0b719;
    --white: #ffffff;
  }
  * { box-sizing: border-box; margin: 0; padding: 0; }
  html, body { width: 1200px; height: 1000px; overflow: hidden; }
  body { background: var(--stage); position: relative; font-family: "Crimson Text", Georgia, serif; }

  .preview-label {
    position: absolute;
    background: var(--label-bg);
    color: var(--white);
    font-family: "Lato", Arial, sans-serif;
    font-weight: 300;
    font-size: 24px;
    letter-spacing: 1px;
    padding: 6px 12px;
  }
  .preview-label--front { left: 60px; top: 40px; }
  .preview-label--back { right: 60px; top: 500px; }

  .card {
    position: absolute;
    width: 560px;
    height: 320px;
    overflow: hidden;
    box-shadow: 0 10px 30px rgba(0,0,0,.45);
  }

  /* Front */
  .card--front {
    left: 60px; top: 90px;
    background: var(--gold);
  }
  .front-brand {
    position: absolute;
    left: 0; right: 0; top: 70px;
    display: flex; align-items: center; justify-content: center; gap: 14px;
  }
  .front-brand__dot {
    width: 34px; height: 34px; border-radius: 50%;
    background: var(--brown);
  }
  .front-brand__name {
    font-family: "Cinzel", Georgia, serif;
    font-weight: 600;
    font-size: 30px;
    color: var(--brown);
    letter-spacing: 1px;
  }
  .front-info {
    position: absolute;
    left: 0; right: 0; top: 186px; height: 96px;
    background: var(--cream);
    display: flex; flex-direction: column; align-items: center; justify-content: center;
    color: var(--brown);
    font-size: 17px;
    line-height: 1.3;
    text-align: center;
  }
  .front-info .sep { padding: 0 8px; }

  /* Back */
  .card--back {
    left: 580px; top: 560px;
    background: radial-gradient(ellipse at 50% 45%, var(--gold-light), var(--gold-deep));
  }
  .back-bar { position: absolute; left: 0; right: 0; height: 14px; background: var(--brown); }
  .back-bar--top { top: 0; }
  .back-bar--bottom { bottom: 0; }
  .person {
    position: absolute; top: 36px; left: 0; right: 0;
    text-align: center; color: var(--brown);
  }
  .person__name {
    font-family: "Cinzel", Georgia, serif;
    font-weight: 600; font-size: 26px; letter-spacing: 1px;
  }
  .person__role {
    font-size: 20px; letter-spacing: 7px; margin-top: -2px;
  }
  .rule {
    position: absolute; left: 110px; right: 110px;
    border-top: 1px dashed var(--orange);
  }
  .rule--top { top: 118px; }
  .rule--bottom { top: 268px; }
  .contact-list {
    position: absolute; top: 134px; left: 150px;
    list-style: none;
  }
  .contact-item {
    display: flex; align-items: center; gap: 18px;
    height: 40px;
    font-size: 19px; font-weight: 600; letter-spacing: 4px;
    color: var(--brown);
  }
  .contact-item--mobile { color: var(--red); }
  .contact-item--email { letter-spacing: 0.5px; font-size: 18px; }
  .contact-item svg { width: 20px; height: 20px; flex: none; }
</style>
</head>
<body>

<div class="preview-label preview-label--front">FRONT PREVIEW</div>
<section class="card card--front" aria-label="Business card front">
  <div class="front-brand">
    <span class="front-brand__dot"></span>
    <span class="front-brand__name">BROSMERE HOLDINGS INC.</span>
  </div>
  <div class="front-info">
    <p>1187 Larkin Rd. Pell Hollow, WI 54872</p>
    <p>Office: (608) 555-0417<span class="sep">|</span>Fax: (608) 555-0283</p>
    <p>Email: brosmereoffice@quillpost.example</p>
  </div>
</section>

<div class="preview-label preview-label--back">BACK PREVIEW</div>
<section class="card card--back" aria-label="Business card back">
  <div class="back-bar back-bar--top"></div>
  <div class="person">
    <p class="person__name">DARREN HOLT</p>
    <p class="person__role">President</p>
  </div>
  <div class="rule rule--top"></div>
  <ul class="contact-list">
    <li class="contact-item contact-item--phone">
      <svg viewBox="0 0 24 24" aria-hidden="true"><path fill="#5b1f0c" d="M6.6 10.8c1.4 2.8 3.8 5.1 6.6 6.6l2.2-2.2c.3-.3.7-.4 1-.2 1.1.4 2.3.6 3.6.6.6 0 1 .4 1 1V20c0 .6-.4 1-1 1C10.6 21 3 13.4 3 4c0-.6.4-1 1-1h3.5c.6 0 1 .4 1 1 0 1.3.2 2.5.6 3.6.1.3 0 .7-.2 1z"/></svg>
      <span>0 31 55 01 42</span>
    </li>
    <li class="contact-item contact-item--mobile">
      <svg viewBox="0 0 24 24" aria-hidden="true"><rect x="6" y="2" width="12" height="20" rx="2" fill="none" stroke="#d52a18" stroke-width="2"/><line x1="10" y1="18.5" x2="14" y2="18.5" stroke="#d52a18" stroke-width="2"/></svg>
      <span>0 400 555 017</span>
    </li>
    <li class="contact-item contact-item--email">
      <svg viewBox="0 0 24 24" aria-hidden="true"><path fill="#e0832a" d="M12 2a7 7 0 0 0-7 7c0 5 7 13 7 13s7-8 7-13a7 7 0 0 0-7-7zm0 9.5A2.5 2.5 0 1 1 12 6.5a2.5 2.5 0 0 1 0 5z"/></svg>
      <span>darrenholt@quillpost.example</span>
    </li>
  </ul>
  <div class="rule rule--bottom"></div>
  <div class="back-bar back-bar--bottom"></div>
</section>

</body>
</html>
```